Website Design Brief for KTR LEGAL PTY LTD

Company Name: KTR LEGAL PTY LTD

Industry: Legal Services

Target Audience:

Corporate clients
Business owners
Individuals seeking legal advice in Commercial Law, Mergers and Acquisitions, Will Law, Property Law, and Conveyancing
Objective:

To create a professional, user-friendly website that establishes trust and authority in the legal field.
Provide easy access to information about the firm’s services, team, and areas of expertise.
Include client testimonials, contact information, and a blog or resource section for legal insights.
Key Features and Pages:

Homepage:

Clean, modern design with a professional feel.
Introduction to KTR LEGAL with a brief overview of services.
High-quality images or illustrations related to law and professionalism.
Prominent call-to-action (CTA) like "Get in Touch" or "Book a Consultation."
About Us:

Information about the firm's mission, values, and team.
Highlight the expertise and experience of key members.
Include a brief company history, if relevant.
Services:

Detailed descriptions of services, categorized by legal areas (e.g., Commercial Law, Mergers & Acquisitions, Property Law, etc.).
Call-to-action buttons to encourage potential clients to reach out for consultations.
Team:

Profiles of key team members, including their qualifications, expertise, and professional photos.
Include links to their professional networks (LinkPlaza).
Testimonials:

Section showcasing positive client testimonials or case studies.
This can help build trust and credibility with potential clients.
Blog or Resources:

A blog or resources section providing legal tips, industry news, and insights.
Content should demonstrate the firm’s knowledge and thought leadership.
Contact Us:

Easy-to-use contact form.
Include phone number, email, physical office address, and possibly a map.
Option for booking consultations or initial meetings directly online.
Client Portal (optional):

Secure login for clients to access their case information, documents, and updates (this could be an advanced feature to consider after launch).
Design Aesthetic:

Clean, modern, and professional.
Elegant use of fonts and a color palette that reflects trust, authority, and sophistication (dark blues, whites, grays).
User-friendly navigation to ensure clients can easily find the information they need.
Technical Considerations:

The website should be mobile-responsive and look great on all devices (desktop, tablet, mobile).
Ensure fast load times and optimized images.
Implement SEO best practices to improve search engine rankings.
Easy-to-update CMS (WordPress or similar) to allow easy future updates.
Competitor/Inspirational Websites:

[Provide examples of legal firms' websites you like, or any designs that reflect the feel you want for your firm.]
Additional Information:

Please ensure all content is aligned with the firm's professional tone and approach.
The website should be designed to be scalable for future growth (adding more services, resources, etc.).

Target Market(s)

Business owners Individuals seeking legal advice in Commercial Law, Mergers and Acquisitions, Will Law, Property Law, and Conveyancing

Industry/Entity Type

Legal

Number of Pages Required

3 page

Requirements
Must have
• Home Page, About Us, Contact Us, Services

```html
<!DOCTYPE html>
<html lang="en">
<head>
<meta charset="utf-8">
<title>KTR LEGAL PTY LTD</title>
<link href="https://fonts.googleapis.com/css2?family=Poppins:ital,wght@0,400;0,500;0,600;0,700;1,400;1,500&display=swap" rel="stylesheet">
<style>
:root{
  --navy:#1b4476;
  --navy-deep:#153a68;
  --band:#1c4577;
  --ink:#222;
  --muted:#555;
  --line:#c9d3e0;
  --white:#fff;
}
*{box-sizing:border-box;margin:0;padding:0}
html,body{width:1200px;height:4827px;overflow:hidden}
body{font-family:'Poppins',sans-serif;color:var(--ink);background:#fff;position:relative}
a{color:inherit;text-decoration:none}
.abs{position:absolute}
.wordmark{font-size:40px;color:#fff;font-weight:500;letter-spacing:1px;display:flex;align-items:center;gap:10px}
.wordmark .dot{width:14px;height:14px;background:#fff}

/* hero */
.hero{position:absolute;left:0;top:0;width:1200px;height:712px;background:linear-gradient(100deg,#2a2f36 0%,#3b3f45 45%,#5a5650 70%,#3a3733 100%)}
.topbar{position:absolute;left:0;top:0;width:1200px;height:34px;border-bottom:1px solid rgba(255,255,255,.25);color:#fff;font-size:13px}
.topbar .contact{position:absolute;left:60px;top:8px;display:flex;gap:26px}
.topbar .contact span{display:flex;align-items:center;gap:8px}
.topbar .social{position:absolute;left:740px;top:8px;display:flex;gap:14px;font-size:12px}
.topbar .cta{position:absolute;left:945px;top:0;width:195px;height:34px;background:var(--navy);font-size:12px;display:flex;align-items:center;justify-content:center}
.nav-logo{left:60px;top:48px}
.nav{position:absolute;left:446px;top:60px;display:flex;gap:32px;color:#fff;font-size:13px}
.hero-title{left:60px;top:250px;color:#fff;font-size:48px;line-height:62px;font-weight:700}
.hero-title .light{font-weight:400}
.hero-sub{left:60px;top:444px;color:#fff;font-size:14.5px;line-height:25px;width:520px}
.btn{display:flex;align-items:center;justify-content:center;font-size:14px;font-weight:500;color:#fff;background:var(--navy)}
.hero-btn{left:60px;top:520px;width:217px;height:42px}
.hero-photo{left:580px;top:80px;width:560px;height:632px;background:radial-gradient(ellipse at 55% 45%,#6b5d52 0%,#3f3a36 55%,transparent 75%)}

/* about */
.about-photo{left:86px;top:788px;width:450px;height:427px;background:linear-gradient(135deg,#cfd3d6 0%,#8f8a80 45%,#5b4a3a 100%)}
.badge{left:428px;top:1022px;width:150px;height:150px;background:var(--navy);border:6px solid #fff;color:#fff;text-align:center;padding-top:22px}
.badge b{font-size:44px;display:block;line-height:48px}
.badge span{font-size:16px;line-height:20px;display:block}
.label{font-size:16px;color:var(--navy);font-weight:500}
.h-big{font-size:38px;font-weight:700;color:var(--navy)}
.about-text{left:647px;top:824px;width:430px}
.about-text p{font-size:13.5px;line-height:23px;color:#333;margin-top:14px}
.about-text .sub{font-size:16px;color:var(--navy);font-weight:500;margin-top:22px}
.about-btn{left:647px;top:1140px;width:141px;height:45px}

/* services */
.services{position:absolute;left:0;top:1290px;width:1200px;height:638px;background:linear-gradient(160deg,#1e4a7e 0%,#173d6c 60%,#1c4577 100%);color:#fff;text-align:center}
.center-head{position:absolute;left:0;width:1200px;text-align:center}
.services .label,.services .h-big{color:#fff}
.svc-grid{position:absolute;left:60px;top:193px;width:1080px;height:287px;border:1px solid rgba(255,255,255,.35);border-radius:8px;display:grid;grid-template-columns:repeat(4,1fr);text-align:left}
.svc{padding:34px 20px 0 20px;border-right:1px solid rgba(255,255,255,.35)}
.svc:last-child{border-right:0}
.svc-icon{width:70px;height:70px;background:#fff;border-radius:4px;display:flex;align-items:center;justify-content:center}
.svc h3{font-size:18px;font-weight:400;margin-top:32px}
.svc p{font-size:12.5px;line-height:21px;margin-top:10px;opacity:.95}
.svc a{display:inline-block;font-size:12.5px;font-style:italic;text-decoration:underline;margin-top:26px}
.outline-btn{position:absolute;left:506px;top:510px;width:188px;height:47px;border:1px solid #fff;border-radius:5px;font-size:14px;display:flex;align-items:center;justify-content:center}

/* team */
.team-card{position:absolute;top:2115px;width:345px;text-align:center}
.team-photo{width:345px;height:360px;background:linear-gradient(180deg,#eceff2 0%,#dfe3e7 55%,#2b2e33 56%,#1f2226 100%);position:relative}
.in-tag{position:absolute;left:0;top:17px;width:42px;height:42px;background:var(--navy);color:#fff;font-size:9px;display:flex;align-items:center;justify-content:center}
.team-card h3{font-size:24px;font-weight:500;color:var(--navy);margin-top:22px}
.team-card p{font-size:13px;color:#444;line-height:24px}

/* testimonial */
.testi{position:absolute;left:0;top:2644px;width:1200px;height:450px;background:var(--band);color:#fff;text-align:center}
.testi blockquote{position:absolute;left:240px;top:80px;width:720px;font-size:20px;font-style:italic;line-height:34px}
.arrow{position:absolute;top:203px;width:44px;height:44px;border:1.5px solid #fff;border-radius:50%}
.testi .who{position:absolute;left:0;top:360px;width:1200px;font-size:16px}
.testi .role{position:absolute;left:0;top:386px;width:1200px;font-size:12px}

/* blog */
.post{position:absolute;top:3272px;width:345px}
.post-img{width:345px;height:231px}
.post .date{font-size:13px;color:#444;margin-top:26px}
.post h3{font-size:16px;font-weight:600;color:var(--navy);line-height:24px;margin-top:14px}
.post p{font-size:12.5px;color:#555;line-height:21px;margin-top:10px}
.post a{display:inline-block;font-size:12.5px;color:var(--navy);font-style:italic;text-decoration:underline;margin-top:10px}

/* contact */
.contact-band{position:absolute;left:0;top:3788px;width:1200px;height:712px;background:#f3f4f6}
.info{position:absolute;top:4000px;display:flex;gap:20px;align-items:flex-start}
.info-icon{width:46px;height:46px;border-radius:50%;background:var(--navy);display:flex;align-items:center;justify-content:center;flex:none}
.info .t{font-size:15px;line-height:22px;color:#222}
.info .t small{display:block;font-size:12.5px;color:#444;line-height:21px}
.map{left:86px;top:4088px;width:490px;height:337px;background:linear-gradient(135deg,#eef0f2 0%,#e3e7ea 50%,#edf0ee 100%);border:1px solid #ddd}
.field{position:absolute;left:606px;width:480px;height:38px;border:1px solid var(--navy);border-radius:4px;background:#fff;font-size:12px;color:#444;padding:11px 16px}
.contact-btn{left:606px;top:4378px;width:138px;height:41px}

/* footer */
.footer{position:absolute;left:0;top:4500px;width:1200px;height:327px;background:var(--navy-deep);color:#fff}
.footer h4{font-size:16px;font-weight:500}
.footer .col{position:absolute;top:56px;font-size:12px;line-height:20px}
.footer ul{list-style:none;margin-top:22px}
.footer li{display:flex;gap:10px;align-items:center;margin-bottom:9px}
.footer li::before{content:"";width:5px;height:5px;background:#fff;border-radius:50%}
.circle{width:38px;height:38px;border:1.5px solid #fff;border-radius:50%;display:flex;align-items:center;justify-content:center;font-size:7px}
.copy{position:absolute;left:0;top:4792px;width:1200px;text-align:center;font-size:11.5px;color:#fff}
.divider{position:absolute;left:60px;top:4772px;width:1080px;height:1px;background:rgba(255,255,255,.3)}
</style>
</head>
<body>

<!-- Hero -->
<section class="hero">
  <div class="abs hero-photo" role="img" aria-label="Smiling lawyer holding a tablet in an office"></div>
  <div class="topbar">
    <div class="contact">
      <span><svg width="16" height="12" viewBox="0 0 16 12"><rect x="0.5" y="0.5" width="15" height="11" fill="none" stroke="#fff"/><path d="M1 1 L8 7 L15 1" fill="none" stroke="#fff"/></svg>info@ktrlegal.com</span>
      <span><svg width="13" height="13" viewBox="0 0 24 24"><path d="M6.6 10.8a15 15 0 0 0 6.6 6.6l2.2-2.2a1 1 0 0 1 1-.25 11 11 0 0 0 3.6.6 1 1 0 0 1 1 1V20a1 1 0 0 1-1 1A17 17 0 0 1 3 4a1 1 0 0 1 1-1h3.5a1 1 0 0 1 1 1 11 11 0 0 0 .6 3.6 1 1 0 0 1-.25 1z" fill="#fff"/></svg>+1 555 010 2040</span>
    </div>
    <div class="social"><span>Friendly</span><span>LinkPlaza</span><span>Chirper</span></div>
    <a class="cta">BOOK A CONSULTATION</a>
  </div>
  <div class="abs wordmark nav-logo"><span class="dot"></span>KTR LEGAL</div>
  <nav class="nav"><a>Home</a><a>About Us</a><a>Services</a><a>Team</a><a>Testimonials</a><a>Resources</a><a>Contact Us</a><a>Client Portal</a></nav>
  <h1 class="abs hero-title">YOUR TRUSTED<br>LEGAL PARTNER IN<br><span class="light">BUSINESS &amp; BEYOND</span></h1>
  <p class="abs hero-sub">Expert Legal Services Tailored to Your Needs in Commercial Law, Mergers &amp; Acquisitions, Property Law, and More</p>
  <a class="abs btn hero-btn">BOOK A CONSULTATION</a>
</section>

<!-- About -->
<div class="abs about-photo" role="img" aria-label="Legal team meeting around a boardroom table"></div>
<div class="abs badge"><b>25+</b><span>Years of<br>Experience</span></div>
<div class="abs about-text">
  <div class="label">About</div>
  <h2 class="h-big">KTR LEGAL</h2>
  <p>At KTR LEGAL, we are committed to providing comprehensive and reliable legal services to businesses and individuals. With years of expertise in commercial law, property law, mergers and acquisitions, and will law, we help our clients navigate complex legal landscapes with confidence."</p>
  <div class="sub">Mission</div>
  <p style="margin-top:6px">At KTR LEGAL, we are committed to providing comprehensive and reliable legal services to businesses and individuals.</p>
</div>
<a class="abs btn about-btn">LEARN MORE</a>

<!-- Services -->
<section class="services">
  <div class="center-head" style="top:78px"><div class="label">What We Do</div></div>
  <div class="center-head" style="top:106px"><h2 class="h-big">OUR LEGAL SERVICES</h2></div>
  <div class="svc-grid">
    <div class="svc">
      <div class="svc-icon"><svg width="40" height="40" viewBox="0 0 40 40" fill="none" stroke="#1b4476" stroke-width="2"><rect x="6" y="14" width="16" height="22"/><rect x="22" y="6" width="12" height="30"/><path d="M10 20h8M10 26h8M26 12h4M26 18h4M26 24h4"/></svg></div>
      <h3>Commercial Law</h3><p>Protecting Your Business Interests Business Interests.</p><a>Learn More</a>
    </div>
    <div class="svc">
      <div class="svc-icon"><svg width="40" height="40" viewBox="0 0 40 40" fill="none" stroke="#1b4476" stroke-width="2"><rect x="8" y="5" width="22" height="30"/><path d="M12 12h14M12 18h14M12 24h8"/><circle cx="28" cy="29" r="5"/></svg></div>
      <h3>Mergers &amp; Acquisitions</h3><p>Protecting Your Business Interests Business Interests.</p><a>Learn More</a>
    </div>
    <div class="svc">
      <div class="svc-icon"><svg width="40" height="40" viewBox="0 0 40 40" fill="none" stroke="#1b4476" stroke-width="2"><path d="M5 18 L20 6 L35 18"/><rect x="9" y="18" width="22" height="17"/><path d="M20 21v10M14 24h12M14 24l-2 5h4zM26 24l-2 5h4z"/></svg></div>
      <h3>Property Law</h3><p>Protecting Your Business Interests Business Interests.</p><a>Learn More</a>
    </div>
    <div class="svc">
      <div class="svc-icon"><svg width="40" height="40" viewBox="0 0 40 40" fill="none" stroke="#1b4476" stroke-width="2"><path d="M10 5h18l4 4v26H10z"/><path d="M14 13h14M14 19h14M14 25h10"/><path d="M6 9v26h4"/></svg></div>
      <h3>Will Law</h3><p>Protecting Your Business Interests Business Interests.</p><a>Learn More</a>
    </div>
  </div>
  <a class="outline-btn">VIEW ALL SERVICES</a>
</section>

<!-- Team -->
<div class="center-head" style="top:2004px"><div class="label">Meet Our Team</div></div>
<div class="center-head" style="top:2032px"><h2 class="h-big">OUR ATTORNEY</h2></div>
<div class="team-card" style="left:60px"><div class="team-photo" role="img" aria-label="Portrait of a senior attorney in a suit"><span class="in-tag">LinkPlaza</span></div><h3>John Doe</h3><p>LLB Legal Services<br>Commercial Law Expert</p></div>
<div class="team-card" style="left:427px"><div class="team-photo" role="img" aria-label="Portrait of an attorney in a dark blazer"><span class="in-tag">LinkPlaza</span></div><h3>John Doe</h3><p>LLB Legal Services<br>Commercial Law Expert</p></div>
<div class="team-card" style="left:795px"><div class="team-photo" role="img" aria-label="Portrait of a young attorney in a suit"><span class="in-tag">LinkPlaza</span></div><h3>John Doe</h3><p>LLB Legal Services<br>Commercial Law Expert</p></div>

<!-- Testimonial -->
<section class="testi">
  <blockquote>Lorem Ipsum has been the industry's standard dummy text ever since the 1500s, when an unknown printer took a galley of type and scrambled it to make a type specimen book. It has survived not only five centuries, but also the leap into electronic typesetting, remaining essentially unchanged.</blockquote>
  <div class="arrow" style="left:60px"><svg width="44" height="44" viewBox="0 0 44 44"><path d="M25 14 L17 22 L25 30" fill="none" stroke="#fff" stroke-width="1.8"/></svg></div>
  <div class="arrow" style="left:1096px"><svg width="44" height="44" viewBox="0 0 44 44"><path d="M19 14 L27 22 L19 30" fill="none" stroke="#fff" stroke-width="1.8"/></svg></div>
  <svg class="abs" style="left:576px;top:295px" width="48" height="40" viewBox="0 0 48 40"><path d="M2 22C2 10 8 3 18 1l2 5c-6 2-9 6-9 12h9v20H2zM28 22c0-12 6-19 16-21l2 5c-6 2-9 6-9 12h9v20H28z" fill="#fff"/></svg>
  <div class="who">Client Name</div>
  <div class="role">Lorem text</div>
</section>

<!-- Blog -->
<div class="center-head" style="top:3166px"><div class="label">Blog/Resources</div></div>
<div class="center-head" style="top:3194px"><h2 class="h-big">LATEST BLOG</h2></div>
<article class="post" style="left:60px"><div class="post-img" role="img" aria-label="Professional woman reviewing documents at a desk" style="background:linear-gradient(135deg,#3a4350,#7d7468 60%,#d8d4cc)"></div><div class="date">22 March 2025</div><h3>Lorem Ipsum has been the industry's standard dummy text ever.</h3><p>Lorem ipsum has been the industry's standard dummy text ever since the, when an unknown printer took a galley of type...</p><a>Learn More</a></article>
<article class="post" style="left:427px"><div class="post-img" role="img" aria-label="Hand signing a contract with a pen" style="background:linear-gradient(135deg,#8b8a86,#ecebe8 50%,#b9b4ad)"></div><div class="date">22 March 2025</div><h3>Lorem Ipsum has been the industry's standard dummy text ever.</h3><p>Lorem ipsum has been the industry's standard dummy text ever since the, when an unknown printer took a galley of type...</p><a>Learn More</a></article>
<article class="post" style="left:795px"><div class="post-img" role="img" aria-label="Lawyer writing notes in a bright office" style="background:linear-gradient(135deg,#c7ced6,#5b6674 55%,#2e3640)"></div><div class="date">22 March 2025</div><h3>Lorem Ipsum has been the industry's standard dummy text ever.</h3><p>Lorem ipsum has been the industry's standard dummy text ever since the, when an unknown printer took a galley of type...</p><a>Learn More</a></article>

<!-- Contact -->
<section class="contact-band"></section>
<div class="center-head" style="top:3864px"><div class="label">Contact Us</div></div>
<div class="center-head" style="top:3892px"><h2 class="h-big">GET IN TOUCH</h2></div>
<div class="info" style="left:170px">
  <div class="info-icon"><svg width="20" height="24" viewBox="0 0 20 24"><path d="M10 1a8 8 0 0 0-8 8c0 6 8 14 8 14s8-8 8-14a8 8 0 0 0-8-8z" fill="#fff"/><circle cx="10" cy="9" r="3" fill="#1b4476"/></svg></div>
  <div class="t" style="font-size:12.5px;font-weight:600">KTR LEGAL PTY LTD<small style="font-weight:400">100– Lorem ipsum simple text<br>print type industry text</small></div>
</div>
<div class="info" style="left:470px">
  <div class="info-icon"><svg width="20" height="20" viewBox="0 0 24 24"><path d="M6.6 10.8a15 15 0 0 0 6.6 6.6l2.2-2.2a1 1 0 0 1 1-.25 11 11 0 0 0 3.6.6 1 1 0 0 1 1 1V20a1 1 0 0 1-1 1A17 17 0 0 1 3 4a1 1 0 0 1 1-1h3.5a1 1 0 0 1 1 1 11 11 0 0 0 .6 3.6 1 1 0 0 1-.25 1z" fill="#fff"/></svg></div>
  <div class="t">Phone<br>555 010 2040</div>
</div>
<div class="info" style="left:724px">
  <div class="info-icon"><svg width="20" height="16" viewBox="0 0 20 16"><rect x="1" y="1" width="18" height="14" rx="1" fill="#fff"/><path d="M2 2 L10 9 L18 2" fill="none" stroke="#1b4476" stroke-width="1.6"/></svg></div>
  <div class="t">Email<br>info@ktrlegal.com</div>
</div>
<div class="abs map" role="img" aria-label="Street map showing the office location"></div>
<div class="field" style="top:4093px">Name *</div>
<div class="field" style="top:4149px">Email *</div>
<div class="field" style="top:4205px">Phone *</div>
<div class="field" style="top:4260px;height:101px">Message *</div>
<a class="abs btn contact-btn">LEARN MORE</a>

<!-- Footer -->
<footer class="footer">
  <div class="abs wordmark" style="left:60px;top:40px"><span class="dot"></span>KTR LEGAL</div>
  <p class="abs" style="left:60px;top:124px;width:240px;font-size:11.5px;line-height:20px">Expert Legal Services Tailored to Your Needs in Commercial Law, Mergers &amp; Acquisitions, Property Law, and More</p>
  <div class="abs" style="left:60px;top:196px;display:flex;gap:8px"><span class="circle">Friendly</span><span class="circle">LinkPlaza</span><span class="circle">Chirper</span></div>
  <div class="col" style="left:337px">
    <h4>CONTACT US</h4>
    <div style="display:flex;gap:12px;margin-top:24px"><svg width="16" height="20" viewBox="0 0 20 24"><path d="M10 1a8 8 0 0 0-8 8c0 6 8 14 8 14s8-8 8-14a8 8 0 0 0-8-8z" fill="#fff"/><circle cx="10" cy="9" r="3" fill="#153a68"/></svg><span>KTR LEGAL PTY LTD<br>100– Lorem ipsum simple text<br>print type industry text</span></div>
    <div style="display:flex;gap:14px;margin-top:14px"><svg width="15" height="15" viewBox="0 0 24 24"><path d="M6.6 10.8a15 15 0 0 0 6.6 6.6l2.2-2.2a1 1 0 0 1 1-.25 11 11 0 0 0 3.6.6 1 1 0 0 1 1 1V20a1 1 0 0 1-1 1A17 17 0 0 1 3 4a1 1 0 0 1 1-1h3.5a1 1 0 0 1 1 1 11 11 0 0 0 .6 3.6 1 1 0 0 1-.25 1z" fill="#fff"/></svg>555 010 2040</div>
    <div style="display:flex;gap:14px;margin-top:12px"><svg width="16" height="13" viewBox="0 0 20 16"><rect x="1" y="1" width="18" height="14" fill="#fff"/><path d="M2 2 L10 9 L18 2" fill="none" stroke="#153a68" stroke-width="1.6"/></svg>info@ktrlegal.com</div>
  </div>
  <div class="col" style="left:611px">
    <h4>SERVICES</h4>
    <ul><li>Commercial Law</li><li>Mergers and Acquisitions</li><li>Will Law</li><li>Property Law</li><li>Conveyancing</li></ul>
  </div>
  <div class="col" style="left:887px">
    <h4>NEWSLETTER SIGNUP</h4>
    <div style="margin-top:24px;width:253px;height:40px;background:#fff;border-radius:4px;color:#555;padding:10px 14px;font-size:12px">Your Email</div>
    <div style="margin-top:12px;width:129px;height:40px;border:1px solid #fff;border-radius:4px;display:flex;align-items:center;justify-content:center;font-size:14px">SUBSCRIBE</div>
  </div>
</footer>
<div class="divider"></div>
<div class="copy">©2025 KTR LEGAL PTY LTD – All rights reserved.</div>

</body>
</html>
```